KVORB Student Exchange needs a brochure design

I need a brochure design for KVORB Student Exchange based in Auckland, New Zealand. I am responsible for outbound exchanges where I recruit local students from around New Zealand between the ages of 15 and 18 who are interested in going on an exchange overseas. Students can select from 12 different countries including America, France, Italy, the Netherlands, Spain, Ireland, Germany, Brazil Japan, and Argentina and choose the programme length from 3 months to an academic year (although we offer shorter programmes for some countries). I would like to attract students who are keen to learn about other cultures and experience something completely different to home. I would like to see vibrant colours and images that coveys fun, youthfulness and adventure.
Updates

Hi,

I have added pics and content for your viewing. 

Thanks.

Tessa

Hi,

Could I request that the designs are done on a tri-fold brochure

Also, I would like to see vibrant colours. So far, I have seen colours matching the logo (which is ok)  but I want to try and move away from that and start something fresh. Please look at the booklet and fee sheet which I have uploaded for ideas. 

I am wondering whether there is too much writing to fit on a tri fold brochure...
If you are having problems fitting everything in, please let me know.

I think the testimonial section could use up 2 spaces on the brochure. 

Target Market(s)

I would like to target teenagers who are interested in other cultures and want to enhance their language learning

Industry/Entity Type

Learn

Font styles to use
Serif
Sans Serif
Decorative

```html
<!DOCTYPE html>
<html lang="en">
<head>
<meta charset="utf-8">
<title>KVORB Student Exchange – Tri-fold Brochure</title>
<link rel="stylesheet" href="https://fonts.googleapis.com/css2?family=Signika:wght@600;700&family=Open+Sans:wght@400;600;700&display=swap">
<style>
  :root{
    --orange:#f7941d;
    --orange-dark:#e07c0c;
    --blue:#3a9cc8;
    --yellow:#f4c518;
    --green:#8db33a;
    --ink:#333333;
    --paper:#ffffff;
    --backdrop:#ece9e4;
  }
  *{box-sizing:border-box;margin:0;padding:0}
  html,body{width:1200px;height:900px;overflow:hidden;background:var(--backdrop)}
  body{font-family:"Open Sans",Arial,sans-serif;color:var(--ink)}
  .sheet{position:absolute;top:40px;left:28px;display:flex;gap:24px;height:820px}
  .cover{width:160px;height:100%;background:var(--orange);position:relative;box-shadow:0 4px 14px rgba(0,0,0,.18)}
  .cover__photo{position:absolute;left:0;right:0;top:430px;height:190px;background:linear-gradient(135deg,#d8c7a6,#a98b62)}
  .cover__contact{position:absolute;left:14px;bottom:28px;right:10px;font-size:8px;line-height:1.5;color:#1f1f1f}
  .cover__name{font-family:"Signika",Arial,sans-serif;font-weight:700;font-size:15px;margin-bottom:4px;display:flex;align-items:center;gap:6px}
  .cover__name::before{content:"";width:10px;height:10px;border-radius:50%;background:#1f1f1f}
  .spread{display:flex;height:100%;box-shadow:0 4px 14px rgba(0,0,0,.18)}
  .panel{width:160px;height:100%;background:var(--paper);overflow:hidden;position:relative;font-size:6.4px;line-height:1.38}
  .panel p{padding:0 8px;margin-bottom:4px}
  .sub{color:var(--orange-dark);font-weight:700;padding:0 8px;margin:4px 0 2px;font-size:6.8px}
  .bar{background:var(--orange);color:#fff;font-family:"Signika",Arial,sans-serif;font-weight:700;font-size:7.4px;letter-spacing:.3px;padding:3px 8px;margin:6px 0 4px;text-transform:uppercase}
  .heading{font-family:"Signika",Arial,sans-serif;font-weight:700;text-transform:uppercase;color:#fff;font-size:10px;padding:8px}
  .heading--blue{background:var(--blue)}
  .heading--orange{background:var(--orange)}
  .why-box{background:var(--blue);color:#fff;padding:2px 8px 8px}
  .why-box strong{font-size:8px;display:block;margin-bottom:3px}
  .why-box ul{list-style:none}
  .why-box li{padding-left:8px;position:relative}
  .why-box li::before{content:"";position:absolute;left:0;top:3px;width:3px;height:3px;background:#fff;border-radius:50%}
  .photo{width:100%}
  .photo--group{height:170px;background:linear-gradient(160deg,#d9c4a0,#a88460)}
  .photo--kimono{height:120px;background:linear-gradient(135deg,#e8b7b3,#b45a6a)}
  .photo--snow{height:130px;background:linear-gradient(180deg,#bcd3e8,#6b7d92)}
  .photo--city{height:140px;background:linear-gradient(180deg,#8fb2cf,#b58d5c)}
  .photo--family{height:140px;background:linear-gradient(135deg,#8a3b33,#3d2a24)}
  .yellow-box{background:var(--yellow);padding:10px 0 6px;margin-bottom:6px}
  .yellow-box .sub{color:#7a4b00}
  .process{position:absolute;left:0;right:0;top:140px;bottom:0;background:var(--green);color:#fff;text-align:center;padding:14px 8px}
  .process::after{content:"";position:absolute;left:0;right:0;bottom:0;height:10px;background:var(--yellow)}
  .process h2{font-family:"Signika",Arial,sans-serif;font-weight:700;font-size:15px;line-height:1.1;margin-bottom:14px}
  .process ol{list-style:none;font-family:"Signika",Arial,sans-serif;font-weight:600;font-size:8.6px;line-height:1.2}
  .process li{margin-bottom:10px;text-transform:uppercase}
</style>
</head>
<body>
<main class="sheet">

  <section class="cover" aria-label="Back cover">
    <div class="cover__photo" role="img" aria-label="Photo of a group of exchange students sitting on a stone wall"></div>
    <div class="cover__contact">
      <div class="cover__name">KVORB</div>
      14 Harbour Lane | PO Box 4021<br>
      Auckland, New Zealand<br>
      www.kvorb-exchange.example<br>
      Phone: 09 555 0148<br>
      E-mail: info@kvorb.example
    </div>
  </section>

  <div class="spread">

    <section class="panel panel--why">
      <h2 class="heading heading--blue">Why go on an exchange?</h2>
      <div class="why-box">
        <strong>Students will:</strong>
        <ul>
          <li>Learn independence and maturity</li>
          <li>Adapt to a whole new culture</li>
          <li>Discover a new country and see exciting sights</li>
          <li>Become fluent in a foreign language</li>
          <li>Make life-long friends across the world</li>
          <li>Gain an edge in future study and work</li>
          <li>Return with a broader view of life</li>
        </ul>
      </div>
      <p style="margin-top:6px">Going overseas builds skills that last a lifetime. Living with a new family and going to a new school will stretch you, surprise you and show you what you are capable of.</p>
      <div class="sub">Understanding of the culture</div>
      <p>You will see a country from the inside, not as a tourist, sharing daily life with locals.</p>
      <div class="sub">A perspective on your life in New Zealand</div>
      <p>Time away helps you value home and see it with fresh eyes when you return.</p>
      <div class="sub">A new family experience</div>
      <p>Your host family becomes a second family who will stay in your life for years.</p>
      <div class="sub">New friends</div>
      <p>You will meet students from your host school and from exchange groups worldwide.</p>
      <div class="photo photo--group" role="img" aria-label="Photo of exchange students posing together outdoors"></div>
    </section>

    <section class="panel panel--when">
      <div class="photo photo--kimono" role="img" aria-label="Photo of students wearing traditional Japanese kimono"></div>
      <h2 class="heading heading--orange">When should I go on an exchange?</h2>
      <p style="margin-top:5px">There are lots of options and we can help you choose the best timing for your studies and goals.</p>
      <div class="bar">Things to consider</div>
      <p>Think about your NCEA plans, your subjects and how long you would like to stay away from home.</p>
      <div class="bar">In Year 11</div>
      <p>Going young means you pick up the language fast and settle in easily. Many students find this a great time to start.</p>
      <div class="bar">In Year 12</div>
      <p>This is a popular year to go. Talk to your school about credits and how to fit the year in with your plans.</p>
      <div class="photo photo--snow" role="img" aria-label="Photo of a group of students standing in the snow"></div>
      <div class="bar">In Year 13</div>
      <p>An exchange after school is a gap year with purpose, before you start university or work.</p>
    </section>

    <section class="panel panel--info">
      <div class="yellow-box">
        <div class="sub">The language you learn is yours for life</div>
        <p>Most students return fluent after a year. Even a short stay makes a real difference to your skills and confidence.</p>
      </div>
      <div class="bar">Language</div>
      <p>If you don't speak the local language yet, don't worry. Classes and daily life help you learn quickly.</p>
      <div class="bar">Host family</div>
      <p>Families are carefully chosen volunteers who welcome you into their home as one of their own.</p>
      <div class="bar">School</div>
      <p>You attend a local high school, take regular classes and join in clubs, sport and events.</p>
      <div class="bar">Departure</div>
      <p>Most programmes leave in January or July. We help with flights, visas and orientation before you go.</p>
      <div class="bar">What if I miss home?</div>
      <p>Feeling homesick is normal. Our partners and your host family support you every step of the way.</p>
      <div class="bar">Costs</div>
      <p>See our fee sheet for prices by country and programme length, from three months to a full year.</p>
    </section>

    <section class="panel panel--process">
      <div class="photo photo--city" role="img" aria-label="Photo of a historic European city square"></div>
      <div class="process">
        <h2>THE EXCHANGE PROCESS</h2>
        <ol>
          <li>Initial application</li>
          <li>Full application</li>
          <li>Interview</li>
          <li>Acceptance</li>
          <li>Application to affiliate in host country</li>
          <li>Book air tickets</li>
          <li>Acceptance in host country</li>
          <li>Locate host family and host school</li>
          <li>Arrange visa documents</li>
          <li>Apply for visa</li>
          <li>Pay for tickets</li>
          <li>Orientation in NZ</li>
          <li>Fly out</li>
          <li>Orientation and transfer to host family</li>
          <li>Monitoring</li>
          <li>Return home, smiling happily</li>
        </ol>
      </div>
    </section>

    <section class="panel panel--stories">
      <div class="photo photo--family" role="img" aria-label="Photo of an exchange student with a host family at Christmas"></div>
      <div class="bar">Sophie – France</div>
      <p>My year in France was the best thing I have ever done. My host family treated me like a daughter and I now speak French every day.</p>
      <div class="bar">James – Germany</div>
      <p>I was nervous at first, but school was fun and I made friends from all over the world during my stay.</p>
      <div class="bar">Aroha – Japan</div>
      <p>Everything was different, from the food to the classes. I learned so much about myself and came home more confident.</p>
      <div class="bar">Liam – Brazil</div>
      <p>Football, beaches and a big loud family. I already miss them and plan to visit again next summer.</p>
      <div class="bar">Emma – Spain</div>
      <p>Learning Spanish was hard at first, but by Christmas I was dreaming in it. I would go again tomorrow.</p>
    </section>

    <section class="panel panel--more">
      <div class="bar" style="margin-top:10px">Hannah – Italy</div>
      <p>Italy taught me to slow down and enjoy life. The food, the people and the history were amazing.</p>
      <div class="bar">Ben – Argentina</div>
      <p>I joined the school rugby team and travelled with my host family to the mountains and the coast.</p>
      <div class="bar">Grace – Netherlands</div>
      <p>Cycling to school every day with my host sister is one of my favourite memories of the year.</p>
      <div class="bar">Parents say</div>
      <p>Our son came home more mature, independent and thankful. It was worth every cent and every tear at the airport.</p>
      <div class="bar">Ireland &amp; America</div>
      <p>Students in English speaking countries enjoy a new school system, new sports and plenty of travel.</p>
      <div class="bar">Choose your country</div>
      <p>Pick from twelve countries and from three months to a full academic year, with shorter options in some places.</p>
      <div class="bar">Get in touch</div>
      <p>Contact us to find out more, request a fee sheet or book a chat about your own exchange adventure.</p>
    </section>

  </div>
</main>
</body>
</html>
```